Design business card using existing logo.

PLEASE DO NOT USE "RED WHITE & BLACK" color combo! Thank you.

Try different color combos such as:
- Vintage colors like brown, orange, gold, blue (not all together but a combo of 1 or 3
- Blue, w/ grey, or silver or white, Blue monochromatic can work as well.
- Use monochromatic variations on back (just an idea)

- Include full name, "Quillmarsh Records" on at least one side.

Target Market(s)

Teens

Industry/Entity Type

Business

Colors
3277b5
ffc214
f04a50
f78f20

```html
<!DOCTYPE html>
<html lang="en">
<head>
<meta charset="utf-8">
<title>Quillmarsh Records — Business Card</title>
<link rel="stylesheet" href="https://fonts.googleapis.com/css2?family=Open+Sans:wght@400;700&display=swap">
<style>
  :root {
    --backdrop: #1e1f22;
    --card-light: #eef1f4;
    --card-dark: #3b3e43;
    --card-dark-deep: #32353a;
    --accent: #3277b5;
    --text-light: #ffffff;
    --text-soft: #dfe6ee;
  }
  * { margin: 0; padding: 0; box-sizing: border-box; }
  html, body { width: 1200px; height: 900px; overflow: hidden; }
  body {
    background: var(--backdrop);
    font-family: "Open Sans", sans-serif;
    display: flex;
    flex-direction: column;
    align-items: center;
    justify-content: center;
    gap: 60px;
  }
  .card {
    width: 630px;
    height: 360px;
    border-radius: 22px;
    overflow: hidden;
    position: relative;
    box-shadow: 0 12px 30px rgba(0,0,0,0.45);
  }
  /* Back side */
  .card-back {
    background: var(--card-dark);
    display: flex;
    align-items: center;
    justify-content: center;
  }
  .back-mark {
    width: 110px;
    height: 110px;
    border-radius: 50%;
    background: var(--card-dark-deep);
    box-shadow: inset 0 2px 4px rgba(0,0,0,0.5), 0 1px 0 rgba(255,255,255,0.06);
  }
  /* Front side */
  .card-front { display: flex; background: var(--card-dark); }
  .brand-panel {
    width: 352px;
    height: 100%;
    background: linear-gradient(160deg, #f8fafc 0%, var(--card-light) 60%, #e1e6eb 100%);
    display: flex;
    flex-direction: column;
    align-items: center;
    justify-content: center;
    gap: 20px;
  }
  .brand-dot {
    width: 84px;
    height: 84px;
    border-radius: 50%;
    background: var(--accent);
  }
  .brand-name {
    font-family: "Open Sans", sans-serif;
    font-weight: 700;
    font-size: 30px;
    line-height: 1.15;
    letter-spacing: 1px;
    text-align: center;
    color: var(--accent);
  }
  .divider-gap { width: 4px; background: var(--card-light); }
  .divider { width: 4px; height: 100%; background: var(--accent); }
  .contact-panel {
    flex: 1;
    padding: 70px 20px 0 44px;
    color: var(--text-light);
  }
  .person-name { font-weight: 700; font-size: 24px; letter-spacing: 0.5px; }
  .person-role { font-size: 16px; margin-top: 2px; color: var(--text-soft); }
  .address { font-size: 16px; line-height: 1.45; margin-top: 22px; color: var(--text-soft); }
  .contact-list { list-style: none; margin-top: 18px; font-size: 16px; line-height: 1.6; color: var(--text-soft); }
  .contact-list li { display: flex; align-items: center; gap: 12px; }
  .contact-list svg { width: 14px; height: 14px; flex: none; }
</style>
</head>
<body>
  <section class="card card-back">
    <div class="back-mark"></div>
  </section>

  <section class="card card-front">
    <div class="brand-panel">
      <div class="brand-dot"></div>
      <div class="brand-name">QUILLMARSH<br>RECORDS</div>
    </div>
    <div class="divider-gap"></div>
    <div class="divider"></div>
    <div class="contact-panel">
      <div class="person-name">Ellis Harrow</div>
      <div class="person-role">Manager</div>
      <p class="address">14 Lantern Lane, Reed Park<br>Marshfield, CA 90417.</p>
      <ul class="contact-list">
        <li>
          <svg viewBox="0 0 24 24" fill="#fff"><path d="M6.6 10.8a15 15 0 0 0 6.6 6.6l2.2-2.2c.3-.3.7-.4 1-.2 1.1.4 2.3.6 3.6.6.6 0 1 .4 1 1V20c0 .6-.4 1-1 1A17 17 0 0 1 3 4c0-.6.4-1 1-1h3.5c.6 0 1 .4 1 1 0 1.3.2 2.5.6 3.6.1.3 0 .7-.2 1z"/></svg>
          +1 555 0142 7781
        </li>
        <li>
          <svg viewBox="0 0 24 24" fill="#fff"><path d="M2 5h20v14H2zm2 2v.5l8 5 8-5V7zm0 2.8V17h16V9.8l-8 5z"/></svg>
          hello@quillmarsh.com
        </li>
        <li>
          <svg viewBox="0 0 24 24" fill="none" stroke="#fff" stroke-width="2"><circle cx="12" cy="12" r="9"/><path d="M3 12h18M12 3c3 3 3 15 0 18M12 3c-3 3-3 15 0 18"/></svg>
          www.quillmarsh.com
        </li>
      </ul>
    </div>
  </section>
</body>
</html>
```